RE Business cards
Q&A Business cards
Project: RE Business cards
RE Business cards  - Real Estate
Creative Brief
Professional
Linda Morrow
Broker/HOMEBROKER®
1187 Ridgefern Avenue Suite 310 Westlake Village, CA 91361
(805) 555-0147 Direct
Linda@MorrowandPartners.example
www.LindaMorrow.example
CA BRE Lic # 07315926
We just need the two business cards. NO Stationary (was already completed). For business cards- Company license # needs to be listed also: CA BRE Lic # 07648203 1st card- Linda's photo (would like to see which picture looks better to have on card) A second card needs to be made for: Dale Morrow Real Estate Agent CA BRE Lic # 07220574 (818) 555-0183 email- Dale@MorrowandPartners.example fax # and address is the same
lmorrow lmorrow
Thank you for all the GREAT submissions! We've notified the designer that we're going to be using to complete the project. Designer was chosen based on their concept submitted that is similar to our other products to help with branding. We just didn't want anyone to continue working on this project when we knew which way we were going. Thanks again....really great work!
We'd like a two sided card. Our previous cards had our company logo large and in the center with the license # underneath in smaller font on one side and the agent info/picture on the other side (company logo was also on that side). For Linda's picture, if you can take out the lower portion to not show the jeans in the picture :)
Looking to brand ourselves with our marketing pieces so I'd like for our business cards to tie in (perhaps in colors?) somewhat to the marketing postcard that was just completed.

```html
<!DOCTYPE html>
<html lang="en">
<head>
<meta charset="utf-8">
<title>Morrow &amp; Partners business cards</title>
<link rel="stylesheet" href="https://fonts.googleapis.com/css2?family=Great+Vibes&family=Cormorant+Garamond:wght@500;600&display=swap">
<style>
  :root {
    --page: #ffffff;
    --frame: #8a8a8a;
    --card: #000000;
    --shadow: rgba(0, 0, 0, 0.45);
    --sky: #3a9fd0;
    --sky-soft: #6fb8dc;
    --green: #2f7a5a;
    --faint: #262626;
    --label: #c9d6dc;
  }
  * { margin: 0; padding: 0; box-sizing: border-box; }
  html, body { width: 1200px; height: 878px; overflow: hidden; background: var(--page); }
  .canvas {
    position: relative;
    width: 1200px; height: 878px;
    border: 2px solid var(--frame);
    font-family: "Cormorant Garamond", "Times New Roman", serif;
  }
  .card {
    position: absolute;
    top: 312px;
    height: 257px;
    background: var(--card);
    box-shadow: 6px 8px 10px var(--shadow);
    overflow: hidden;
  }
  .card--front { left: 108px; width: 449px; }
  .card--back { left: 643px; width: 456px; }

  .brand-mark {
    position: absolute;
    left: 50%; top: 46px;
    width: 96px; height: 96px;
    margin-left: -48px;
    border: 6px solid var(--green);
    border-radius: 50%;
  }
  .brand-name {
    position: absolute;
    left: 0; right: 0; top: 172px;
    text-align: center;
    color: var(--sky);
    font-size: 40px;
    font-weight: 600;
    letter-spacing: 4px;
  }

  .brand-watermark {
    position: absolute;
    left: 30px; top: 80px;
    color: var(--faint);
    font-size: 64px;
    font-weight: 600;
    letter-spacing: 4px;
  }
  .agent-name {
    position: absolute;
    left: 150px; top: 42px;
    color: var(--sky);
    font-family: "Great Vibes", cursive;
    font-size: 52px;
    font-weight: 400;
    line-height: 1;
    white-space: nowrap;
  }
  .contact {
    position: absolute;
    left: 296px; top: 134px;
    width: 150px;
    list-style: none;
  }
  .contact li {
    display: flex;
    align-items: baseline;
    min-height: 19px;
  }
  .contact .label {
    flex: 0 0 56px;
    color: var(--label);
    font-size: 14px;
    font-weight: 600;
    line-height: 1.2;
    white-space: nowrap;
  }
  .contact .item--web .label {
    flex: 0 0 auto;
    margin-right: 6px;
  }
  .contact .value {
    flex: 1 1 auto;
    min-width: 0;
    color: var(--sky-soft);
    font-size: 6px;
    line-height: 1.15;
    overflow-wrap: anywhere;
  }
</style>
</head>
<body>
<div class="canvas">
  <section class="card card--front" aria-label="Card front">
    <div class="brand-mark" aria-hidden="true"></div>
    <div class="brand-name">M &amp; P</div>
  </section>

  <section class="card card--back" aria-label="Card back">
    <div class="brand-watermark" aria-hidden="true">M &amp; P</div>
    <h1 class="agent-name">Linda Morrow</h1>
    <ul class="contact">
      <li><span class="label">Address</span><span class="value">1187 Ridgefern Avenue Suite 310 Westlake Village, CA 91361</span></li>
      <li><span class="label">Phone</span><span class="value">(805) 555-0147</span></li>
      <li><span class="label">Fax</span><span class="value">(818) 555-0183</span></li>
      <li><span class="label">Email</span><span class="value">Linda@MorrowandPartners.example</span></li>
      <li class="item--web"><span class="label">Web address</span><span class="value">www.LindaMorrow.example</span></li>
    </ul>
  </section>
</div>
</body>
</html>
```